Web Design - Fitness for Middle Age Women

I need a web design for a start-up personal training company in Los Alamitos, CA called 'Maple Fitness & Health.' I would like to cater personal training services to middle-age mothers (30-50 years of age) who have kids and who would also want their children to receive services. The attached file is the logo of the company. Keep in mind the theme colors are white and blue and black, but make the background/pictures appealing to middle-age mothers. I want the flow of the website to be easy to use. The final design should present the company as a professional personal training service.

I realize this is a low budget project for designers but this is a budget I have to offer at the moment and if I take your design I will make sure to come back to improve the site when I'm able to gain more capital. I am looking for a full website built (using wordpress) with the following tabs (About / FAQ / Services / Clients / Location / Contact Us...and social media links to Twitter / Instagram / Facebook)
Updates

I am looking over the current designs and narrowing down the decision. A decision will be made in the next 24-48 hours.

Target Market(s)

Middle-age mothers (30-55 years of age) who have children, an established career (or husband who is the bread-winner of the house) and has forgotten to take care of themselves and their body for years. I want them to realize lifestyle change is a choice, and it is a choice they need to make for themselves and their family to be a proper pattern for their children.

Industry/Entity Type

Fitness

Requirements
Must have
• The logo I have attached.

```html
<!DOCTYPE html>
<html lang="en">
<head>
<meta charset="utf-8">
<title>Maple Fitness &amp; Health</title>
<link href="https://fonts.googleapis.com/css2?family=Cinzel:wght@400;700&family=Arimo:wght@400;700&family=Roboto+Condensed:wght@700&display=swap" rel="stylesheet">
<style>
:root{
  --navy:#16125a;
  --royal:#2a2190;
  --ink:#333;
  --muted:#666;
  --btn-grey:#6e6e6e;
  --footer-bg:#ececec;
  --red:#e0101a;
  --white:#fff;
}
*{box-sizing:border-box;margin:0;padding:0}
html,body{width:922px;height:1200px;overflow:hidden;background:var(--white)}
body{position:relative;font-family:Arimo,Arial,sans-serif;color:var(--ink)}
h1,h2,h3{font-weight:400}
.abs{position:absolute}
.topline{left:0;top:0;width:922px;height:5px;background:var(--navy)}
.brand{left:80px;top:22px;display:flex;align-items:center;gap:10px}
.brand-dot{width:58px;height:58px;border-radius:50%;background:var(--navy)}
.brand-name{font-family:Cinzel,serif;font-size:15px;line-height:18px;color:var(--ink)}
.nav{left:313px;top:35px;width:534px;height:39px;display:flex;background:linear-gradient(#8d8d8d,#6d6d6d)}
.nav a{font-family:Cinzel,serif;font-size:11px;color:var(--white);text-decoration:none;display:flex;align-items:center;padding:0 13.5px;white-space:nowrap}
.nav a.active{background:var(--navy);padding:0 18px}
.hero{left:76px;top:100px;width:771px;height:342px;background:linear-gradient(90deg,#8a8a8a 0%,#a9a9a9 35%,#c9b2a3 60%,#bfa69a 100%)}
.hero-copy{left:92px;top:168px;width:224px;text-align:center;color:var(--white)}
.hero-title{font-family:Cinzel,serif;font-size:21px;letter-spacing:.5px;margin-bottom:14px;white-space:nowrap}
.hero-text{font-family:Cinzel,serif;font-size:10px;line-height:20px}
.hero-btn{left:128px;top:345px;width:144px;height:30px;background:var(--white);font-family:Cinzel,serif;font-size:9.5px;color:var(--ink);display:flex;align-items:center;justify-content:center}
.dots{left:181px;top:399px;display:flex;gap:6px}
.dots span{width:7px;height:7px;border-radius:50%;background:var(--white)}
.dots span:first-child{background:#555}
.welcome-title{left:0;width:922px;top:458px;text-align:center;font-family:Cinzel,serif;font-size:13.5px;color:#555;letter-spacing:.5px}
.welcome-text{left:160px;width:602px;top:485px;text-align:center;font-size:8.6px;line-height:16.5px;color:#444}
.grey-btn{background:var(--btn-grey);color:var(--white);display:flex;align-items:center;justify-content:center;font-size:9px}
.read-more{left:416px;top:546px;width:96px;height:29px}
.section-title{left:76px;top:598px;font-family:Cinzel,serif;font-size:12.5px;color:#555}
.card{width:237px;height:150px}
.card-photo{width:100%;height:113px}
.card-label{height:37px;background:var(--royal);color:var(--white);font-family:Cinzel,serif;font-size:11.5px;letter-spacing:.5px;display:flex;align-items:center;justify-content:center}
.list{left:617px;top:620px;list-style:none}
.list li{display:flex;align-items:center;gap:16px;height:22.4px;font-family:Cinzel,serif;font-size:12px;color:#555;letter-spacing:.3px}
.list li.current{color:var(--royal)}
.list svg{width:14px;height:12px}
.offers{left:607px;top:783px;width:206px;height:170px;border:1px solid #ccc;padding:10px 14px}
.offers h3{font-family:Cinzel,serif;font-size:12.5px;color:#555;margin-bottom:8px}
.offers p{font-size:8.5px;line-height:16.5px;color:#555}
.offers .more{width:54px;height:16px;margin:3px 0 13px 2px;font-size:8px}
.footer{left:0;top:968px;width:922px;height:184px;background:var(--footer-bg)}
.col-title{font-family:Cinzel,serif;font-size:13px;color:#333;white-space:nowrap}
.col-text{font-size:8.6px;line-height:14px;color:#555}
.email-field{left:341px;top:1058px;width:143px;height:23px;background:var(--white);border:1px solid #ccc;font-size:8.5px;color:#888;padding:6px 5px}
.subscribe{left:484px;top:1058px;width:63px;height:23px;background:var(--red);color:var(--white);font-size:9.5px;display:flex;align-items:center;justify-content:center}
.field{left:600px;width:238px;height:31px;background:var(--white);border-radius:2px;font-size:8.8px;color:#777;padding:11px 10px}
.submit{left:600px;top:1102px;width:68px;height:31px;background:var(--btn-grey);color:var(--white);font-family:'Roboto Condensed',sans-serif;font-size:11.5px;display:flex;align-items:center;justify-content:center}
.bottom{left:0;top:1152px;width:922px;height:48px;background:linear-gradient(#555,#6a6a6a)}
.copyright{left:78px;top:1169px;font-size:8px;color:var(--white)}
.social{left:764px;top:1164px;display:flex;gap:7px}
.social span{width:19px;height:19px;background:#8fa0c4;border-radius:2px}
</style>
</head>
<body>
<div class="abs topline"></div>

<header>
  <div class="abs brand">
    <div class="brand-dot"></div>
    <div class="brand-name">Maple<br>Fitness &amp; Health</div>
  </div>
  <nav class="abs nav">
    <a class="active" href="#">Home</a><a href="#">About</a><a href="#">FAQ</a><a href="#">Services</a><a href="#">Clients</a><a href="#">Location</a><a href="#">Contact Us</a>
  </nav>
</header>

<section>
  <div class="abs hero" role="img" aria-label="Photo of four smiling women of different ages posing together"></div>
  <div class="abs hero-copy">
    <h1 class="hero-title">Lorem ipsum dolor</h1>
    <p class="hero-text">consectetur adipiscing elit, sed do eiusmod tempor incididunt ut labore et dolore magna aliqua. Ut enim ad minim veniam, quis nostrud exercitation ullamco laboris nisi ut aliquip ex ea commodo consequat.</p>
  </div>
  <div class="abs hero-btn">Click more info</div>
  <div class="abs dots"><span></span><span></span><span></span></div>
</section>

<section>
  <h2 class="abs welcome-title">WELCOME TO OUR MAPLE FITNESSAND HEALTH</h2>
  <p class="abs welcome-text">Summit Personal Training has been a leading personal training company in the fitness industry for over 15 years. Based in Central London and South West London, Summit Training offers every aspect of fitness. Summit Training offers an exclusive personal training experience for people who are serious about improving their health and bodies.</p>
  <div class="abs grey-btn read-more">READ MORE</div>
</section>

<section>
  <h2 class="abs section-title">Personal Training Services</h2>
  <div class="abs card" style="left:76px;top:625px"><div class="card-photo" role="img" aria-label="Woman doing push-ups in a gym" style="background:linear-gradient(120deg,#7a7a7a,#c7bfb8 50%,#555)"></div><div class="card-label">Personal Training</div></div>
  <div class="abs card" style="left:344px;top:625px"><div class="card-photo" role="img" aria-label="Colleagues working together at a desk" style="background:linear-gradient(120deg,#6b4f3c,#d9b7a0 50%,#c9a888)"></div><div class="card-label">Corporate Fitness</div></div>
  <div class="abs card" style="left:76px;top:803px"><div class="card-photo" role="img" aria-label="Woman doing yoga by the sea" style="background:linear-gradient(#e9d8a8,#9fb7b0 45%,#2f6f78 75%,#8a7a60)"></div><div class="card-label">Kids Fitness</div></div>
  <div class="abs card" style="left:345px;top:803px"><div class="card-photo" role="img" aria-label="Doctor consulting with a client" style="background:linear-gradient(90deg,#3a2a22,#d9cfc4 55%,#eee8e0)"></div><div class="card-label">Personal Training</div></div>

  <ul class="abs list">
    <li class="current"><svg viewBox="0 0 14 12"><path d="M1 6l4 4 8-9" fill="none" stroke="#16125a" stroke-width="2.4"/></svg>Personal Training</li>
    <li><svg viewBox="0 0 14 12"><path d="M1 6l4 4 8-9" fill="none" stroke="#777" stroke-width="2.4"/></svg>Corporate Fitness</li>
    <li><svg viewBox="0 0 14 12"><path d="M1 6l4 4 8-9" fill="none" stroke="#777" stroke-width="2.4"/></svg>Nutritional Advice</li>
    <li><svg viewBox="0 0 14 12"><path d="M1 6l4 4 8-9" fill="none" stroke="#777" stroke-width="2.4"/></svg>Virtual Personal Training</li>
    <li><svg viewBox="0 0 14 12"><path d="M1 6l4 4 8-9" fill="none" stroke="#777" stroke-width="2.4"/></svg>Worldwide Trainers</li>
    <li><svg viewBox="0 0 14 12"><path d="M1 6l4 4 8-9" fill="none" stroke="#777" stroke-width="2.4"/></svg>Kids Fitness</li>
  </ul>

  <aside class="abs offers">
    <h3>SPECIAL OFFERS</h3>
    <p>Autumn / Winter offer 2014 30 Personal Training Sessions - Only £750.</p>
    <div class="grey-btn more">MORE</div>
    <p>Autumn / Winter offer 2014 30 Personal Training Sessions - Only £750.</p>
    <div class="grey-btn more">MORE</div>
  </aside>
</section>

<footer>
  <div class="abs footer"></div>
  <h3 class="abs col-title" style="left:79px;top:990px">Why Evergreen Training?</h3>
  <p class="abs col-text" style="left:79px;top:1014px;width:245px">We are the UK's leading training provider delivering a wide range of Traineeships, Apprenticeships and training courses that have been developed to make a real impact.<br><br>We have developed the skills and careers of thousands of individuals and have improved the performance of some of the biggest, and smallest, employers in the UK across a wide range of business sectors</p>

  <h3 class="abs col-title" style="left:342px;top:991px">Newsletter</h3>
  <p class="abs col-text" style="left:341px;top:1017px;width:210px">Ut enim ad minim veniam, quis nostrud exercitation ullamco laboris aliquip</p>
  <div class="abs email-field">Enter your Email Id</div>
  <div class="abs subscribe">Subscribe</div>

  <h3 class="abs col-title" style="left:601px;top:993px">Find out how we can help</h3>
  <div class="abs field" style="top:1018px">Name</div>
  <div class="abs field" style="top:1058px">Email</div>
  <div class="abs submit">SUBMIT</div>

  <div class="abs bottom"></div>
  <p class="abs copyright">Copyright 2014 by maple fitness and health.&nbsp; All rights reserved.</p>
  <div class="abs social" aria-label="Social links"><span></span><span></span><span></span></div>
</footer>
</body>
</html>
```